Oil and Gas Industry training School Needs a Web Design

We need a web design for a new company based in Northern British Columbia Canada called "SKILLPATH Trade Academy Inc." Is a training facility that specializes in different aspects of Pipeline Construction training. We also offer compliance courses for Oil and Gas Industry. We would like to see designs that us the colours in our logo.

Target Market(s)

Is Men and women between 18-60 that want to work in the oil and gas industry

Industry/Entity Type

School

Number of Pages Required

5+ page

Font styles to use
Sans Serif

Colors
f37022
000000
333333
ffffff
848484
7f7f7f
c8c8c8
f68d4d
fee3d4

Requirements
Must have
• a easy back end for editing content! and adding additional pages if necessary.

```html
<!DOCTYPE html>
<html lang="en">
<head>
<meta charset="utf-8">
<title>SKILLPATH Trade Academy Inc.</title>
<link href="https://fonts.googleapis.com/css2?family=Open+Sans:wght@400;600;700;800&display=swap" rel="stylesheet">
<style>
:root{
  --orange:#f37022;
  --orange-light:#f68d4d;
  --orange-pale:#fee3d4;
  --black:#000000;
  --ink:#333333;
  --white:#ffffff;
  --grey:#848484;
  --grey-2:#7f7f7f;
  --grey-line:#c8c8c8;
  --page:#f2f2f2;
  --footer:#2b2b2b;
  --footer-deep:#1f1f1f;
}
*{box-sizing:border-box;margin:0;padding:0}
html,body{width:822px;height:1200px;overflow:hidden}
body{background:var(--page);font-family:"Open Sans",Arial,sans-serif;color:var(--ink);font-size:8px;line-height:1.45;position:relative}
.wrap{width:572px;margin:0 auto;position:relative}

.topbar{height:22px;background:var(--white);border-bottom:1px solid #e6e6e6}
.topbar .wrap{display:flex;justify-content:space-between;align-items:center;height:22px;font-size:7px;color:var(--grey)}
.socials{display:flex;gap:4px}
.socials span{width:10px;height:10px;border-radius:2px;background:#d8d8d8;display:block}

.header{height:66px;background:var(--white)}
.header .wrap{display:flex;justify-content:space-between;align-items:center;height:66px}
.brand{display:flex;align-items:center;gap:6px}
.brand-mark{width:18px;height:18px;border-radius:50%;background:var(--orange)}
.brand-name{font-weight:800;font-size:16px;color:var(--ink);letter-spacing:.5px;line-height:1}
.brand-sub{font-size:6px;color:var(--orange);font-weight:600;letter-spacing:.3px}
.nav{display:flex;gap:14px;font-size:7px;font-weight:600;text-transform:uppercase;color:var(--ink)}
.nav a{color:inherit;text-decoration:none;padding:6px 4px}
.nav a.active{background:var(--orange);color:var(--white)}

.hero{height:300px;position:relative;overflow:hidden}
.hero-photo{position:absolute;inset:0;background:linear-gradient(180deg,#c9ccce 0%,#a4a9ac 45%,#7f8384 100%)}
.hero-copy{position:absolute;left:0;right:0;top:150px;text-align:center;color:var(--white);font-weight:700;font-size:12px;letter-spacing:.4px;text-transform:uppercase;line-height:1.7}
.hero-copy .line{display:inline-block;background:rgba(0,0,0,.55);padding:0 8px}
.btn{display:inline-block;font-weight:600;font-size:8px;padding:6px 14px;text-decoration:none}
.btn-solid{background:var(--orange);color:var(--white)}
.btn-outline{border:1px solid var(--orange);color:var(--orange);background:var(--white)}
.hero .btn{margin-top:16px}
.arrow{position:absolute;top:138px;width:14px;height:24px;background:rgba(0,0,0,.45);display:flex;align-items:center;justify-content:center}
.arrow.prev{left:0}.arrow.next{right:0}
.corner{position:absolute;right:0;top:0}

.callout{background:var(--white);margin-top:12px;padding:10px 14px;display:flex;justify-content:space-between;align-items:center;border:1px solid #e2e2e2}
.callout p{font-size:7px;color:var(--grey);width:400px}

.features{display:flex;justify-content:space-between;margin-top:26px}
.feature{width:176px;display:flex;gap:8px}
.feature svg{flex:none}
.feature h3{font-size:10px;font-weight:600;color:var(--ink);margin-bottom:4px}
.feature p{font-size:6.5px;color:var(--grey)}
.more{font-size:6.5px;color:var(--ink);font-weight:600;margin-top:2px;display:block}

.section-title{font-size:10px;font-weight:700;color:var(--ink);padding-bottom:5px;border-bottom:1px solid var(--grey-line);margin-bottom:8px;position:relative}
.section-title::after{content:"";position:absolute;left:0;bottom:-1px;width:40px;height:2px;background:var(--orange)}
.services{margin-top:40px}
.service-grid{display:flex;justify-content:space-between}
.service{width:136px}
.service-photo{height:96px;background:linear-gradient(160deg,#8aa0b4,#5d6770)}
.service:nth-child(2) .service-photo{background:linear-gradient(160deg,#c8a25a,#6c5b44)}
.service:nth-child(3) .service-photo{background:linear-gradient(160deg,#e0b53a,#8a7a55)}
.service:nth-child(4) .service-photo{background:linear-gradient(160deg,#9fb6c8,#53636f)}
.service-cap{padding:4px 6px;background:var(--white);border:1px solid #e2e2e2;border-top:none}
.service-cap h4{font-size:8px;font-weight:700}
.service-cap p{font-size:6px;color:var(--grey)}
.service.featured .service-cap{background:var(--orange);border-color:var(--orange);color:var(--white)}
.service.featured .service-cap p{color:var(--orange-pale)}

.split{display:flex;justify-content:space-between;margin-top:44px}
.news,.why{width:276px}
.post{display:flex;gap:8px;margin-bottom:20px}
.date{width:24px;flex:none;text-align:center;border:1px solid var(--grey-line);background:var(--white)}
.date b{display:block;font-size:9px;color:var(--white);background:var(--ink)}
.date span{font-size:6px;color:var(--grey)}
.post h5{font-size:8px;font-weight:600}
.post p{font-size:6.5px;color:var(--grey)}
.acc-item{border:1px solid #dedede;background:var(--white);margin-bottom:5px}
.acc-head{display:flex;justify-content:space-between;align-items:center;padding:6px 8px;font-size:7.5px;font-weight:600}
.acc-head i{font-style:normal;color:var(--grey)}
.acc-body{padding:5px 8px 9px;font-size:6.5px;color:var(--grey);border-top:1px solid #eee}

.tweetbar{position:absolute;left:0;top:976px;width:822px;height:36px;background:var(--orange);color:var(--white)}
.tweetbar .wrap{display:flex;align-items:center;gap:8px;height:36px;font-size:7px}
.tweet-dot{width:10px;height:10px;border-radius:50%;background:var(--white);flex:none}

.footer{position:absolute;left:0;top:1012px;width:822px;height:188px;background:var(--footer);color:#b5b5b5}
.footer .wrap{display:flex;justify-content:space-between;padding-top:14px}
.fcol{width:128px;font-size:6.5px}
.fcol h6{font-size:8px;color:var(--white);font-weight:700;margin-bottom:8px}
.footer .brand-name{color:var(--white);font-size:13px;margin-bottom:6px}
.thumbs{display:grid;grid-template-columns:repeat(3,38px);gap:4px}
.thumbs span{height:28px;background:linear-gradient(160deg,#7d8a94,#4a5157)}
.fcol ul{list-style:none}
.fcol li{padding:3px 0;border-bottom:1px solid #3b3b3b}
.fsocial{display:flex;gap:4px;margin-top:8px}
.fsocial span{width:10px;height:10px;border-radius:50%;background:#555}
.copyright{position:absolute;left:0;bottom:0;width:822px;height:22px;background:var(--footer-deep);font-size:6px;line-height:1;color:var(--grey-2)}
.copyright .wrap{display:flex;justify-content:space-between;align-items:center;height:22px;padding-top:0}
</style>
</head>
<body>

<div class="topbar">
  <div class="wrap">
    <span>Call Us: +1 (250) 555-0148</span>
    <div class="socials"><span></span><span></span><span></span><span></span><span></span></div>
  </div>
</div>

<header class="header">
  <div class="wrap">
    <div class="brand">
      <span class="brand-mark"></span>
      <div>
        <div class="brand-name">SKILLPATH</div>
        <div class="brand-sub">TRADE ACADEMY INC.</div>
      </div>
    </div>
    <nav class="nav">
      <a class="active">Home</a><a>Courses</a><a>Facility</a><a>Testimonials</a><a>FAQs</a><a>Apply Now</a><a>Contact</a>
    </nav>
  </div>
</header>

<section class="hero">
  <div class="hero-photo" role="img" aria-label="Pipeline facility with two trainees in hard hats and safety vests"></div>
  <svg class="corner" width="26" height="26" viewBox="0 0 26 26"><path d="M0 0H26V26Z" fill="var(--orange)"/></svg>
  <div class="hero-copy">
    <span class="line">Pipeline Design and Construction</span><br>
    <span class="line">Job Training Programs</span><br>
    <a class="btn btn-solid">Apply Now</a>
  </div>
  <div class="arrow prev"><svg width="6" height="10" viewBox="0 0 6 10"><path d="M5 1 1 5l4 4" stroke="#fff" fill="none" stroke-width="1.5"/></svg></div>
  <div class="arrow next"><svg width="6" height="10" viewBox="0 0 6 10"><path d="M1 1l4 4-4 4" stroke="#fff" fill="none" stroke-width="1.5"/></svg></div>
</section>

<main class="wrap">
  <div class="callout">
    <p>Have you ever thought about starting a career in the field? Our short courses give you the skills, safety tickets and hands-on practice to get on site and start your pipeline work.</p>
    <a class="btn btn-outline">Apply Now</a>
  </div>

  <div class="features">
    <div class="feature">
      <svg width="18" height="18" viewBox="0 0 18 18"><rect x="2" y="9" width="3" height="7" fill="var(--orange)"/><rect x="7.5" y="5" width="3" height="11" fill="var(--ink)"/><rect x="13" y="2" width="3" height="14" fill="var(--orange)"/></svg>
      <div><h3>Consulting</h3><p>Expert advice on site safety, crew planning and compliance for pipeline projects of every size in the region.</p><span class="more">Read More...</span></div>
    </div>
    <div class="feature">
      <svg width="18" height="18" viewBox="0 0 18 18"><rect x="2" y="3" width="14" height="10" fill="none" stroke="var(--ink)" stroke-width="1.5"/><path d="M6 16h6M9 13v3" stroke="var(--orange)" stroke-width="1.5"/></svg>
      <div><h3>Training</h3><p>Hands-on classes led by field trades with real equipment, safety tickets and job placement help for every student.</p><span class="more">Read More...</span></div>
    </div>
    <div class="feature">
      <svg width="18" height="18" viewBox="0 0 18 18"><circle cx="9" cy="9" r="6" fill="none" stroke="var(--ink)" stroke-width="1.5"/><circle cx="9" cy="9" r="2.5" fill="var(--orange)"/></svg>
      <div><h3>Products</h3><p>Study guides, safety gear lists and course kits prepared for students and employers across the north.</p><span class="more">Read More...</span></div>
    </div>
  </div>

  <section class="services">
    <h2 class="section-title">Our Services</h2>
    <div class="service-grid">
      <div class="service featured"><div class="service-photo" role="img" aria-label="Crew of workers at a pipeline site"></div><div class="service-cap"><h4>Operations</h4><p>Plant and line operation</p></div></div>
      <div class="service"><div class="service-photo" role="img" aria-label="Workers reviewing plans on site"></div><div class="service-cap"><h4>Maintenance</h4><p>Upkeep and repair skills</p></div></div>
      <div class="service"><div class="service-photo" role="img" aria-label="Rows of yellow hard hats"></div><div class="service-cap"><h4>Products</h4><p>Kits and study guides</p></div></div>
      <div class="service"><div class="service-photo" role="img" aria-label="Technician at an automated control panel"></div><div class="service-cap"><h4>Automation</h4><p>Controls and monitoring</p></div></div>
    </div>
  </section>

  <div class="split">
    <section class="news">
      <h2 class="section-title">Recent News</h2>
      <div class="post">
        <div class="date"><b>07</b><span>JUN</span></div>
        <div><h5>This is a Standard Post</h5><p>New intake dates for spring courses are open. Seats fill fast, so book your spot early and bring your safety boots.</p><span class="more">Read More...</span></div>
      </div>
      <div class="post">
        <div class="date"><b>07</b><span>JUN</span></div>
        <div><h5>Post with Featured Image</h5><p>Our graduates joined a major line project this month. See how the course helped them get on the crew.</p><span class="more">Read More...</span></div>
      </div>
    </section>
    <section class="why">
      <h2 class="section-title">Why Choose Us?</h2>
      <div class="acc-item">
        <div class="acc-head">Why We Are <i>&minus;</i></div>
        <div class="acc-body">Small classes, field instructors and a local training yard mean you learn by doing. We help you earn the tickets employers ask for and connect you with crews hiring now.</div>
      </div>
      <div class="acc-item"><div class="acc-head">Management Team <i>+</i></div></div>
      <div class="acc-item"><div class="acc-head">Why Us? <i>+</i></div></div>
    </section>
  </div>
</main>

<div class="tweetbar">
  <div class="wrap"><span class="tweet-dot"></span><span>Latest from our feed: new safety course dates are posted, register online today and start your pipeline career this season.</span></div>
</div>

<footer class="footer">
  <div class="wrap">
    <div class="fcol">
      <div class="brand-name">SKILLPATH</div>
      <p>SKILLPATH Trade Academy Inc. trains men and women for pipeline construction and oil and gas compliance work across Northern British Columbia.</p>
      <div class="fsocial"><span></span><span></span><span></span><span></span></div>
    </div>
    <div class="fcol">
      <h6>Latest Projects</h6>
      <div class="thumbs" role="img" aria-label="Project photo thumbnails"><span></span><span></span><span></span><span></span><span></span><span></span></div>
    </div>
    <div class="fcol">
      <h6>Recent Posts</h6>
      <ul><li>Spring intake now open</li><li>Graduates join line crew</li><li>New safety ticket course</li><li>Yard upgrades complete</li></ul>
    </div>
    <div class="fcol">
      <h6>Contact Info</h6>
      <ul><li>48 Ridgeline Road, Fort Kestrel, BC</li><li>+1 (250) 555-0148</li><li>info@skillpath-academy.ca</li><li>www.skillpath-academy.ca</li></ul>
    </div>
  </div>
  <div class="copyright"><div class="wrap"><span>&copy; SKILLPATH Trade Academy Inc. All rights reserved.</span><span>Home · Courses · Contact</span></div></div>
</footer>

</body>
</html>
```